Business Cards Letter Head Financial Trading Company
Bus Cards Letter Head Compliment Slips
Simple
Oliver Petchley
Managing Director
Level 52
8 Harrow Crescent
Fenmoor Quay
London
E17 3RT
oliver.petchley@zqtrading.co.uk
www.zoltavequitytrading.co.uk
Would like additional cards for other employees
Logo on back page

```html
<!DOCTYPE html>
<html lang="en">
<head>
<meta charset="utf-8">
<title>Zoltav Equity Trading – Business Card</title>
<link rel="stylesheet" href="https://fonts.googleapis.com/css2?family=Open+Sans:ital,wght@0,400;0,600;0,700;1,400;1,700&display=swap">
<style>
  :root {
    --backdrop: #d9d9dc;
    --card: #ffffff;
    --navy: #2f2a6e;
    --band: #3d3485;
    --gold: #c9932e;
    --text: #3c3c46;
    --muted: #6b6b75;
    --rule: #8a8a92;
  }
  * { box-sizing: border-box; margin: 0; padding: 0; }
  html, body { width: 1200px; height: 901px; overflow: hidden; }
  body {
    background: var(--backdrop);
    font-family: "Open Sans", Arial, sans-serif;
    position: relative;
  }
  .card {
    position: absolute;
    width: 540px;
    height: 340px;
    background: var(--card);
    border-radius: 14px;
    overflow: hidden;
    box-shadow: 0 6px 18px rgba(0,0,0,0.18);
  }
  .card--back { left: 40px; top: 280px; }
  .card--front { left: 620px; top: 280px; }

  .brand {
    position: absolute;
    left: 0; right: 0;
    display: flex;
    align-items: center;
    justify-content: center;
    gap: 12px;
  }
  .brand__dot {
    width: 30px; height: 30px;
    border-radius: 50%;
    background: var(--gold);
  }
  .brand__name {
    color: var(--navy);
    font-weight: 600;
    font-size: 27px;
    letter-spacing: 0.5px;
  }
  .card--back .brand { top: 150px; }
  .card--front .brand { top: 58px; }

  .holder {
    position: absolute;
    right: 280px;
    top: 168px;
    text-align: right;
  }
  .holder__name {
    color: var(--navy);
    font-weight: 700;
    font-style: italic;
    font-size: 16px;
  }
  .holder__role {
    color: var(--muted);
    font-style: italic;
    font-size: 12.5px;
    margin-top: 2px;
  }
  .divider {
    position: absolute;
    left: 276px;
    top: 160px;
    width: 1px;
    height: 108px;
    background: var(--rule);
  }
  .contact {
    position: absolute;
    left: 292px;
    top: 158px;
    color: var(--text);
    font-size: 12px;
    line-height: 16px;
  }
  .contact__address { margin-bottom: 6px; }
  .contact__row {
    display: flex;
    align-items: center;
    gap: 8px;
  }
  .contact__row svg { width: 12px; height: 12px; flex: none; }

  .footer-rule {
    position: absolute;
    left: 0; right: 0;
    top: 290px;
    height: 2px;
    background: var(--gold);
  }
  .footer-band {
    position: absolute;
    left: 0; right: 0;
    top: 294px;
    bottom: 0;
    background: var(--band);
    display: flex;
    align-items: center;
    padding-left: 34px;
  }
  .footer-band__web {
    color: #ffffff;
    font-size: 12.5px;
    letter-spacing: 2.6px;
  }
</style>
</head>
<body>

  <section class="card card--back" aria-label="Card back">
    <div class="brand">
      <span class="brand__dot"></span>
      <span class="brand__name">Zoltav Equity Trading</span>
    </div>
  </section>

  <section class="card card--front" aria-label="Card front">
    <div class="brand">
      <span class="brand__dot"></span>
      <span class="brand__name">Zoltav Equity Trading</span>
    </div>

    <div class="holder">
      <p class="holder__name">Oliver Petchley</p>
      <p class="holder__role">Managing Director</p>
    </div>

    <div class="divider"></div>

    <div class="contact">
      <p class="contact__address">Level 52, 8 Harrow Crescent<br>Fenmoor Quay, London<br>E17 3RT</p>
      <p class="contact__row">
        <svg viewBox="0 0 12 12" aria-hidden="true"><path d="M1 3.5C1 2 2.5 1.5 6 1.5S11 2 11 3.5L9 5 8 4H4L3 5Z M3 6h6l1 4H2Z" fill="var(--text)"/></svg>
        0207 946 0381
      </p>
      <p class="contact__row">
        <svg viewBox="0 0 12 12" aria-hidden="true"><rect x="3" y="0.5" width="6" height="11" rx="1" fill="var(--text)"/><rect x="4" y="2" width="4" height="6" fill="#fff"/></svg>
        44 207 946 0392
      </p>
      <p class="contact__row">
        <svg viewBox="0 0 12 12" aria-hidden="true"><rect x="0.8" y="2.5" width="10.4" height="7" fill="none" stroke="var(--text)" stroke-width="1"/><path d="M1 3l5 3.5L11 3" fill="none" stroke="var(--text)" stroke-width="1"/></svg>
        oliver.petchley@zqtrading.co.uk
      </p>
    </div>

    <div class="footer-rule"></div>
    <div class="footer-band">
      <span class="footer-band__web">www.zoltavequitytrading.co.uk</span>
    </div>
  </section>

</body>
</html>
```